Flyer-Design für Fahrschule gesucht
Zielgruppe
Wir sind eine Fahrschule/ Führerscheinausbildung/ Bildungsträger und benötigen für die verschiedenen Führerscheinklassen einen Informationsflyer.
Aufgabenstellung
Format DIN Lang zum Aufklappen
Der Flyer sollte so gestaltet sein das sich das sich die auf der Front durch Austausch eines Icon/ Logos oder Text die jeweilige Führerscheinklasse bzw Information recht einfach austauschen lässt. Rückseite auch immer gleich. Innendesign auch immer gleich bis auf die Texte die dann jeweils ausgetauscht werden müssen.
Würde ungern Fotos einsetzen da bei Fahrzeug oder personal Wechsel dieses immer wieder zu Problemen führt - ich würde lieber auf Icons setzen da diese dauerhaft bestand haben.

```html
<!DOCTYPE html>
<html lang="de">
<head>
<meta charset="utf-8">
<title>Fahrschule Weitblick – Flyer Klasse B und AM</title>
<link href="https://fonts.googleapis.com/css2?family=Ubuntu:wght@400;500;700&family=Arimo:wght@700&display=swap" rel="stylesheet">
<style>
  :root{
    --page:#e6e6e7;
    --panel:#181a1a;
    --band:#1f1f1f;
    --yellow:#ffe100;
    --olive:#7c7312;
    --white:#ffffff;
    --text:#e9e9e9;
  }
  *{margin:0;padding:0;box-sizing:border-box}
  html,body{width:1200px;height:1200px;overflow:hidden;background:var(--page)}
  body{position:relative;font-family:"Ubuntu",sans-serif;color:var(--text)}
  .panel{position:absolute;background:var(--panel);overflow:hidden}
  .row-b{top:92px}
  .row-am{top:644px}
  .cover{left:103px;width:237px;height:475px}
  .inside{left:364px;width:476px;height:475px}
  .back{left:863px;width:238px;height:475px}

  /* cover */
  .brand-band{position:absolute;left:0;top:52px;width:100%;height:152px;background:var(--band);text-align:center}
  .brand{position:absolute;top:40px;left:0;width:100%;display:flex;justify-content:center;align-items:center;gap:6px}
  .brand-dot{width:12px;height:12px;border-radius:50%;background:var(--yellow)}
  .brand-name{font-weight:700;font-size:17px;color:var(--white);letter-spacing:.2px}
  .tagline{position:absolute;top:100px;width:100%;font-size:8.6px;color:var(--white)}
  .cover-url{position:absolute;top:121px;width:100%;font-size:9.8px;color:var(--yellow)}
  .cover-title{position:absolute;top:292px;width:100%;text-align:center;font-size:18.5px;font-weight:500;color:var(--white);line-height:23px}
  .cover-title .hl{color:var(--yellow);font-weight:700}
  .cover-icon{position:absolute;left:80px;top:374px;width:78px;height:28px;border-radius:14px 18px 8px 8px;background:linear-gradient(180deg,#ffffff 65%,#ffe100 100%)}
  .cover-icon.moped{left:88px;top:365px;width:62px;height:34px;border-radius:17px;background:linear-gradient(90deg,#ffe100 0 40%,#ffffff 40%)}
  .cover-vehicle{position:absolute;top:412px;width:100%;text-align:center;font-size:17px;font-weight:500;color:var(--white)}

  /* inside */
  .head{position:absolute;left:23px;top:22px}
  .head-title{font-size:18.6px;font-weight:500;color:var(--yellow);line-height:22px}
  .head-sub{font-size:12.2px;color:var(--white);line-height:15px}
  .head-icon{position:absolute;left:340px;top:29px;width:113px;height:42px;border-radius:20px 26px 10px 10px;background:linear-gradient(180deg,#ffffff 70%,#ffe100 100%)}
  .head-icon.moped{left:366px;top:24px;width:85px;height:46px;border-radius:22px;background:linear-gradient(90deg,#ffe100 0 45%,#ffffff 45%)}
  .rule{position:absolute;left:0;top:71.5px;width:100%;height:1px;background:var(--yellow)}
  .col{position:absolute;top:100px;font-size:7.8px;line-height:10.5px;color:var(--text)}
  .col-left{left:24px;width:192px}
  .col-right{left:260px;width:196px}
  h3.section{font-size:10.2px;font-weight:500;color:var(--yellow);text-decoration:underline;text-underline-offset:2px;margin-bottom:7px;line-height:13px}
  h4.sub{font-size:9.4px;font-weight:500;color:var(--yellow);margin-bottom:3px;line-height:12px}
  .col p{margin-bottom:10px}
  .y{color:var(--yellow)}
  ul.arrows{list-style:none;margin-bottom:11px}
  ul.arrows li{position:relative;padding-left:11px}
  ul.arrows li::before{content:"";position:absolute;left:3px;top:2.5px;border-left:4px solid var(--yellow);border-top:3px solid transparent;border-bottom:3px solid transparent}
  ul.ticks{list-style:none}
  ul.ticks li{position:relative;padding-left:15px}
  ul.ticks svg{position:absolute;left:3px;top:2px;width:7px;height:6px}

  /* back */
  .big-letter{position:absolute;left:22px;top:-4px;font-family:"Arimo",sans-serif;font-weight:700;font-size:230px;line-height:1;color:var(--olive);transform:scaleX(.72);transform-origin:left top}
  .big-letter.am{left:22px;top:7px;font-size:126px;letter-spacing:-2px;transform:none}
  .contact{position:absolute;left:23px;top:336px;font-size:7.6px;line-height:10.5px;color:var(--white)}
  .contact p{margin-bottom:10.5px}
</style>
</head>
<body>

<section class="panel cover row-b">
  <div class="brand-band">
    <div class="brand"><span class="brand-dot"></span><span class="brand-name">Fahrschule Weitblick</span></div>
    <div class="tagline">Führerschein&nbsp;•&nbsp;Weiterbildung&nbsp;•&nbsp;Qualifizierung</div>
    <div class="cover-url">www.fahrschule-weitblick.de</div>
  </div>
  <h2 class="cover-title">FÜHRERSCHEIN<br>KLASSE <span class="hl">B</span></h2>
  <div class="cover-icon" role="img" aria-label="Icon: weißer PKW mit gelben Felgen"></div>
  <div class="cover-vehicle">PKW</div>
</section>

<section class="panel inside row-b">
  <div class="head">
    <div class="head-title">KLASSE B</div>
    <div class="head-sub">Kraftwagen bis 3,5 t zG</div>
  </div>
  <div class="head-icon" role="img" aria-label="Icon: weißer PKW mit gelben Felgen"></div>
  <div class="rule"></div>

  <div class="col col-left">
    <h3 class="section">FAHRERLAUBNIS FÜR:</h3>
    <p><span class="y">Kraftfahrzeuge</span> – ausgenommen Kraftfahrzeuge der Klassen AM, A1, A2 und A – mit einer zulässigen Gesamtmasse von nicht mehr als <span class="y">3 500 kg</span>, die zur Beförderung von nicht mehr als <span class="y">acht Personen</span> außer dem Fahrzeugführer ausgelegt und gebaut sind (auch mit Anhänger mit einer zulässigen Gesamtmasse von nicht mehr als 750 kg oder mit Anhänger über 750 kg zulässiger Gesamtmasse, sofern 3500 kg zulässige Gesamtmasse der Kombination nicht überschritten wird). Eingeschlossene Klassen: L, AM</p>
    <h4 class="sub">Vorrausetzung</h4>
    <p style="margin-bottom:15px">Mindestalter: 18 Jahre,<br>17 Jahre beim Begleiteten Fahren (BF17)</p>
    <h3 class="section">AUSBILDUNG</h3>
    <h4 class="sub">Theoretische Ausbildung</h4>
    <p style="margin-bottom:0">Theorie/Doppelstunden á 90 Minuten</p>
    <ul class="arrows">
      <li>bei Ersterteilung: 12</li>
      <li>bei Erweiterung: 6</li>
      <li>Zusatzstoff: 2</li>
    </ul>
    <h4 class="sub">Praktische Ausbildung</h4>
    <p style="margin-bottom:0">Eine Fahrstunde entspricht 45 Minuten</p>
    <ul class="arrows">
      <li>Übungsstunden: nach Bedarf</li>
      <li>Überlandfahrt: 5 Fahrstunden</li>
      <li>Autobahnfahrt: 4 Fahrstunden</li>
      <li>Dunkelfahrt: 3 Fahrstunden</li>
    </ul>
  </div>

  <div class="col col-right">
    <h3 class="section">PRÜFUNG</h3>
    <h4 class="sub">Prüfung Theorie</h4>
    <p>bei Ersterteilung: Fragebogen mit 30 Fragen,<br>ab 11 Fehlerpunkten ist die Prüfung nicht bestanden oder bei 2 falsch beantworteten Fragen mit der Wertigkeit 5</p>
    <p>bei Erweiterung: Fragebogen mit 20 Fragen,<br>ab 7 Fehlerpunkten ist die Prüfung nicht bestanden</p>
    <h4 class="sub">Prüfung Praxis</h4>
    <p>Dauer mindestens 45 Minuten<br>Prüfungsinhalte: Sicherheitskontrolle, Fahren innerorts, außerorts auch Autobahnen und Kraftfahrstraßen</p>
    <p>Mit der Ausbildung kann etwa ein halbes Jahr vor Erreichen des Mindestalters begonnen werden.</p>
    <p style="margin-bottom:14px">Die theoretische Prüfung darf frühestens 3 Monate, die praktische Prüfung frühestens einen Monat vor Erreichen des Mindestalters abgelegt werden.</p>
    <h4 class="sub" style="margin-bottom:5px">Unterlagen und Nachweise<br>zur Antragstellung</h4>
    <ul class="ticks">
      <li><svg viewBox="0 0 7 6"><path d="M.5 3l2 2L6.5.8" fill="none" stroke="#ffe100" stroke-width="1.4"/></svg>Personalausweis/Pass</li>
      <li><svg viewBox="0 0 7 6"><path d="M.5 3l2 2L6.5.8" fill="none" stroke="#ffe100" stroke-width="1.4"/></svg>Biometrisches Passbild</li>
      <li><svg viewBox="0 0 7 6"><path d="M.5 3l2 2L6.5.8" fill="none" stroke="#ffe100" stroke-width="1.4"/></svg>Sehtest</li>
      <li><svg viewBox="0 0 7 6"><path d="M.5 3l2 2L6.5.8" fill="none" stroke="#ffe100" stroke-width="1.4"/></svg>Kurs über lebensrettende Sofortmaßnahmen am Unfallort</li>
    </ul>
  </div>
</section>

<section class="panel back row-b">
  <div class="big-letter">B</div>
  <div class="contact">
    <p>Lindenallee 14<br>48100 Auenfeld<br>Tel. 05900 1234560</p>
    <p>Mühlenweg 3<br>48200 Birkenau<br>Tel. 05901 6543210</p>
    <p>www.fahrschule-weitblick.de<br>info@fahrschule-weitblick.de</p>
  </div>
</section>

<section class="panel cover row-am">
  <div class="brand-band">
    <div class="brand"><span class="brand-dot"></span><span class="brand-name">Fahrschule Weitblick</span></div>
    <div class="tagline">Führerschein&nbsp;•&nbsp;Weiterbildung&nbsp;•&nbsp;Qualifizierung</div>
    <div class="cover-url">www.fahrschule-weitblick.de</div>
  </div>
  <h2 class="cover-title">FÜHRERSCHEIN<br>KLASSE <span class="hl">AM</span></h2>
  <div class="cover-icon moped" role="img" aria-label="Icon: Mofa in Weiß und Gelb"></div>
  <div class="cover-vehicle">MOFA/MOPED</div>
</section>

<section class="panel inside row-am">
  <div class="head">
    <div class="head-title">KLASSE AM</div>
    <div class="head-sub">Krafträder (50 cm³)</div>
  </div>
  <div class="head-icon moped" role="img" aria-label="Icon: Mofa in Weiß und Gelb"></div>
  <div class="rule"></div>

  <div class="col col-left">
    <h3 class="section">FAHRERLAUBNIS FÜR:</h3>
    <ul class="arrows">
      <li><span class="y">Zweirädrige Kleinkrafträder</span><br>bis zu 45 km/h und 50 cm³</li>
      <li><span class="y">Fahrräder mit Hilfsmotor</span><br>bis zu 45 km/h und 50 cm³</li>
      <li><span class="y">Dreirädrige Kleinkrafträder</span><br>bis zu 45 km/h und 50 cm³</li>
      <li><span class="y">Vierrädrige Leichtkraftfahrzeuge</span><br>bis zu 45 km/h und 50 cm³</li>
    </ul>
    <h4 class="sub">Vorrausetzung</h4>
    <p style="margin-bottom:17px">Mindestalter: 16 Jahre</p>
    <h3 class="section">AUSBILDUNG</h3>
    <p style="margin-bottom:13px">Mit der Ausbildung kann etwa ein halbes Jahr vor Erreichen des Mindestalters begonnen werden.</p>
    <h4 class="sub">Theoretische Ausbildung</h4>
    <p style="margin-bottom:0">Theorie/Doppelstunden á 90 Minuten</p>
    <ul class="arrows">
      <li>bei Ersterteilung: 12</li>
      <li>bei Erweiterung: 6</li>
      <li>Zusatzstoff: 4</li>
    </ul>
    <h4 class="sub">Praktische Ausbildung</h4>
    <p style="margin-bottom:0">Eine Fahrstunde entspricht 45 Minuten</p>
    <ul class="arrows">
      <li>Übungsstunden: nach Bedarf (die Zahl der Fahrstunden ist abhängig von ihren persönlichen Fähigkeiten und dem Lernfortschritt)</li>
    </ul>
  </div>

  <div class="col col-right">
    <h3 class="section">PRÜFUNG</h3>
    <p style="margin-bottom:14px">Die theoretische Prüfung darf frühestens 3 Monate, die praktische Prüfung frühestens einen Monat vor Erreichen des Mindestalters abgelegt werden.</p>
    <h4 class="sub">Prüfung Theorie</h4>
    <p>bei Ersterteilung: Fragebogen mit 30 Fragen,<br>ab 11 Fehlerpunkten ist die Prüfung nicht bestanden oder bei 2 falsch beantworteten Fragen mit der Wertigkeit 5</p>
    <p>bei Erweiterung: Fragebogen mit 20 Fragen,<br>ab 7 Fehlerpunkten ist die Prüfung nicht bestanden</p>
    <h4 class="sub">Prüfung Praxis</h4>
    <p style="margin-bottom:14px">Dauer mindestens 45 Minuten<br>Prüfungsinhalte: Sicherheitskontrolle, Fahren innerorts,</p>
    <h4 class="sub" style="margin-bottom:5px">Unterlagen und Nachweise<br>zur Antragstellung</h4>
    <ul class="ticks">
      <li><svg viewBox="0 0 7 6"><path d="M.5 3l2 2L6.5.8" fill="none" stroke="#ffe100" stroke-width="1.4"/></svg>Personalausweis/Pass</li>
      <li><svg viewBox="0 0 7 6"><path d="M.5 3l2 2L6.5.8" fill="none" stroke="#ffe100" stroke-width="1.4"/></svg>Biometrisches Passbild</li>
      <li><svg viewBox="0 0 7 6"><path d="M.5 3l2 2L6.5.8" fill="none" stroke="#ffe100" stroke-width="1.4"/></svg>Sehtest</li>
      <li><svg viewBox="0 0 7 6"><path d="M.5 3l2 2L6.5.8" fill="none" stroke="#ffe100" stroke-width="1.4"/></svg>Kurs über lebensrettende Sofortmaßnahmen am Unfallort</li>
    </ul>
  </div>
</section>

<section class="panel back row-am">
  <div class="big-letter am">AM</div>
  <div class="contact">
    <p>Lindenallee 14<br>48100 Auenfeld<br>Tel. 05900 1234560</p>
    <p>Mühlenweg 3<br>48200 Birkenau<br>Tel. 05901 6543210</p>
    <p>www.fahrschule-weitblick.de<br>info@fahrschule-weitblick.de</p>
  </div>
</section>

</body>
</html>
```